Free Legal Consultation

Boris,

I am wondering if you could take the Open House invitation you created for me for KMRD and use it to create a postcard for people stopping in to let us know if they are interested in making a meeting with us.
So, front of the card - left side of the card, we would have the front door picture, then on the right side of the card,we would have the logo, underneath a picture of me,

then two locations:
342 Corbin Rd., Newton, MA
8 Halvering Rd., Norwell, MA
(617) 482-3160.

On the back of the card, on the left side of the card 3 check boxes next to 3 categories:
Estate Planning
Estate and Trust Administration
Elder Law and Nursing Care Planning

On the right side of the card:

I am interested in a free legal consultation:

Name: ______________________________
Address: ____________________________
____________________________
Phone: ____________________________
Email: ____________________________

Can you work up a design for me?

It would be great to have it for the open house.

Thanks, Wendy

```html
<!DOCTYPE html>
<html lang="en">
<head>
<meta charset="utf-8">
<title>KMRD – Free Legal Consultation Postcard</title>
<link rel="stylesheet" href="https://fonts.googleapis.com/css2?family=Questrial&family=Mulish:ital,wght@1,700&display=swap">
<style>
  :root {
    --page-bg: #f2f2f2;
    --brand-red: #7a0708;
    --band-red: rgba(122, 8, 10, 0.78);
    --white: #ffffff;
    --ink-grey: #7a7a7a;
    --label-grey: #8a8a8a;
    --rule-grey: #9a9a9a;
    --photo-dark: #3a3a3a;
    --photo-mid: #6b6b6b;
  }
  * { box-sizing: border-box; margin: 0; padding: 0; }
  html, body { width: 1071px; height: 1200px; overflow: hidden; }
  body {
    background: var(--page-bg);
    font-family: "Questrial", "Century Gothic", sans-serif;
    position: relative;
  }
  .postcard {
    position: absolute;
    left: 214px;
    width: 652px;
    height: 454px;
    overflow: hidden;
    background: var(--white);
    box-shadow: 0 4px 14px rgba(0,0,0,0.18);
  }
  .postcard--front { top: 121px; }
  .postcard--back { top: 642px; }

  /* Front */
  .portrait-photo {
    position: absolute; left: 0; top: 0; width: 362px; height: 100%;
    background: radial-gradient(ellipse at 50% 35%, var(--photo-mid), var(--photo-dark) 75%);
  }
  .door-photo {
    position: absolute; left: 365px; top: 0; right: 0; height: 100%;
    background: linear-gradient(180deg, #8a8a8a 0%, #5a5a5a 45%, #2e2e2e 100%);
  }
  .photo-divider {
    position: absolute; left: 362px; top: 0; width: 3px; height: 100%;
    background: var(--white);
  }
  .info-band {
    position: absolute; left: 0; right: 0; top: 298px; height: 132px;
    background: var(--band-red);
  }
  .brand {
    position: absolute; left: 42px; top: 52px;
    display: flex; align-items: center; gap: 14px;
  }
  .brand__square { width: 34px; height: 34px; background: var(--white); }
  .brand__name {
    color: var(--white); font-size: 50px; letter-spacing: 10px; line-height: 1;
  }
  .locations {
    position: absolute; left: 346px; top: 22px;
    color: var(--white); font-size: 22px; font-style: italic; line-height: 27px;
    letter-spacing: -0.3px;
  }

  /* Back */
  .services-panel {
    position: absolute; left: 0; top: 0; width: 331px; height: 100%;
    background: var(--brand-red);
  }
  .services { list-style: none; position: absolute; left: 23px; top: 194px; }
  .services__item {
    display: flex; align-items: center; gap: 12px;
    height: 38px; color: var(--white); font-size: 16.5px; letter-spacing: -0.3px;
  }
  .services__box { width: 25px; height: 25px; background: var(--white); flex: none; }

  .consult-form { position: absolute; left: 331px; top: 0; right: 0; height: 100%; }
  .consult-form__rule {
    position: absolute; left: 28px; width: 254px; height: 2px; background: var(--brand-red);
  }
  .consult-form__heading {
    position: absolute; left: 28px; top: 54px;
    font-family: "Mulish", sans-serif; font-style: italic; font-weight: 700;
    font-size: 23px; line-height: 22px; color: var(--ink-grey); letter-spacing: -0.8px;
  }
  .field {
    position: absolute; left: 20px; right: 18px;
    display: flex; align-items: flex-end; gap: 4px;
    color: var(--label-grey); font-size: 17px; letter-spacing: -0.3px;
  }
  .field__line { flex: 1; border-bottom: 1px solid var(--rule-grey); height: 1px; margin-bottom: 3px; }
</style>
</head>
<body>

<section class="postcard postcard--front" aria-label="Postcard front">
  <div class="portrait-photo" role="img" aria-label="Black and white portrait photo of the attorney in a dark jacket"></div>
  <div class="door-photo" role="img" aria-label="Black and white photo of the office front door with arched fanlight window and lantern"></div>
  <div class="photo-divider"></div>
  <div class="info-band">
    <div class="brand">
      <span class="brand__square"></span>
      <span class="brand__name">KMRD</span>
    </div>
    <address class="locations">
      342 Corbin Rd., Newton, MA<br>
      8 Halvering Rd., Norwell, MA<br>
      (617) 482-3160.
    </address>
  </div>
</section>

<section class="postcard postcard--back" aria-label="Postcard back">
  <div class="services-panel">
    <ul class="services">
      <li class="services__item"><span class="services__box"></span>Estate Planning</li>
      <li class="services__item"><span class="services__box"></span>Estate and Trust Administration</li>
      <li class="services__item"><span class="services__box"></span>Elder Law and Nursing Care Planning</li>
    </ul>
  </div>
  <div class="consult-form">
    <span class="consult-form__rule" style="top:37px"></span>
    <h2 class="consult-form__heading">I am interested in a<br>free legal consultation:</h2>
    <span class="consult-form__rule" style="top:115px"></span>
    <div class="field" style="top:140px"><span>Name:</span><span class="field__line"></span></div>
    <div class="field" style="top:181px"><span>Address:</span><span class="field__line"></span></div>
    <div class="field" style="top:222px"><span class="field__line"></span></div>
    <div class="field" style="top:264px"><span>Phone:</span><span class="field__line"></span></div>
    <div class="field" style="top:305px"><span>Email:</span><span class="field__line"></span></div>
  </div>
</section>

</body>
</html>
```